Vital Spark Electrical in need of a business card design

We need a new business card designed for our electrical business. We have a logo already which I will attach below.
Would like the business card to be..
-BLACK background preferably, possibly white back ground behind logo if colours clash.
-White & Blue (logo blue) text
Something that makes the logo pop, & a modern look. Possibly minimal clean format.

REQUIRE:
-Logo on front & back

TEXT TO INCLUDE (ON ONE SIDE):

Tom Harlow
Director/Electrician
M: 0417 365 208
E:info@vitalsparkelectrical-example.com.au
W:www.vitalsparkelectrical-example.com.au
R.E.C 57318

Custom/New Homes
Renovations
Commercial Office/Shop Fit-outs
Communications & Security Cameras
Electric Vehicle Chargers
Airconditioning
Updates

Requirements
Nice to have
• Possibly even lighten the grey shades for the words 'Vital' & 'Spark' to be more easily read on a black background.

```html
<!DOCTYPE html>
<html lang="en">
<head>
<meta charset="utf-8">
<title>Vital Spark Electrical – Business Card</title>
<link rel="stylesheet" href="https://fonts.googleapis.com/css2?family=Poppins:wght@400;600&family=Oswald:wght@300;400&display=swap">
<style>
  :root {
    --page-bg: #e6eef8;
    --card-black: #1a1a1c;
    --panel-white: #ffffff;
    --brand-blue: #1aa7e0;
    --brand-slate: #4a5560;
    --text-white: #f4f4f4;
    --text-grey: #8b8e92;
  }
  * { box-sizing: border-box; margin: 0; padding: 0; }
  html, body { width: 1200px; height: 1200px; overflow: hidden; }
  body {
    background: var(--page-bg);
    position: relative;
    font-family: "Poppins", sans-serif;
  }
  .card {
    position: absolute;
    left: 180px;
    width: 840px;
    height: 480px;
    background: var(--card-black);
    border-radius: 40px;
    overflow: hidden;
  }
  .card--front { top: 56px; }
  .card--back { top: 632px; }

  /* Front */
  .front-tab {
    position: absolute;
    left: 391px;
    top: 264px;
    width: 449px;
    height: 136px;
    background: var(--panel-white);
    border-radius: 28px 0 0 28px;
    display: flex;
    align-items: center;
    justify-content: center;
    gap: 16px;
  }
  .brand-square {
    width: 26px;
    height: 26px;
    background: var(--brand-blue);
    flex: none;
  }
  .brand-name {
    font-family: "Poppins", sans-serif;
    font-weight: 600;
    font-size: 25px;
    color: var(--brand-slate);
    white-space: nowrap;
  }

  /* Back */
  .services {
    position: absolute;
    top: 36px;
    left: 0;
    width: 100%;
    list-style: none;
    text-align: center;
    color: var(--text-white);
    font-size: 21px;
    letter-spacing: 1.8px;
    text-transform: uppercase;
  }
  .services li { height: 41.5px; line-height: 32px; }

  .contact-band {
    position: absolute;
    left: 0;
    top: 308px;
    width: 804px;
    height: 138px;
    background: var(--panel-white);
    border-radius: 0 32px 32px 0;
    font-family: "Oswald", sans-serif;
  }
  .person { position: absolute; left: 35px; top: 12px; }
  .person__name {
    color: var(--brand-blue);
    font-weight: 400;
    font-size: 36px;
    line-height: 44px;
  }
  .person__role {
    color: var(--text-grey);
    font-weight: 300;
    font-size: 28px;
    line-height: 34px;
  }
  .person__licence {
    color: var(--text-grey);
    font-weight: 300;
    font-size: 21px;
    line-height: 30px;
    margin-top: 8px;
  }
  .contact-list {
    position: absolute;
    left: 292px;
    top: 16px;
    list-style: none;
    font-weight: 300;
    font-size: 24px;
    line-height: 38px;
    color: var(--card-black);
    letter-spacing: -0.3px;
    white-space: nowrap;
  }
  .contact-list .label { color: var(--brand-blue); margin-right: 4px; }
  .back-square {
    position: absolute;
    right: 40px;
    top: 52px;
    width: 34px;
    height: 34px;
    background: var(--brand-blue);
  }
</style>
</head>
<body>
  <section class="card card--front">
    <div class="front-tab">
      <span class="brand-square"></span>
      <span class="brand-name">Vital Spark Electrical</span>
    </div>
  </section>

  <section class="card card--back">
    <ul class="services">
      <li>Custom/New Homes</li>
      <li>Renovations</li>
      <li>Commercial Office/Shop Fit-outs</li>
      <li>Communications &amp; Security Cameras</li>
      <li>Electric Vehicle Chargers</li>
      <li>Airconditioning</li>
    </ul>
    <div class="contact-band">
      <div class="person">
        <p class="person__name">Tom Harlow</p>
        <p class="person__role">Director/Electrician</p>
        <p class="person__licence">R.E.C 57318</p>
      </div>
      <ul class="contact-list">
        <li><span class="label">E:</span>info@vitalsparkelectrical-example.com.au</li>
        <li><span class="label">W:</span>www.vitalsparkelectrical-example.com.au</li>
        <li><span class="label">M:</span>0417 365 208</li>
      </ul>
      <span class="back-square"></span>
    </div>
  </section>
</body>
</html>
```